Brookvale Insurance Services - Insurance Agency Wesbite

I need a website for my insurance agency called Brookvale Insurance Services. I have attached my company logo. You can use the colors from the copy logo to create the website color scheme. I need a Request A Quote section.
Business Address: 7316 Marlowe Ave Unit D, Studio City Ca 91607
Business Phone: (818) 555-0193
I would need the following drop downs on the main page:

1st drop down:
Business Insurance
⁃ Commercial Auto
⁃ Employment Practice Liability Insurance
⁃ General Liability Insurance
⁃ Professional Liability Insurance
⁃ Property Insurance
⁃ Workers Compensation Insurance

2nd drop down:
Industries We Serve
- Construction
- Janitorial
- Landscapers
- Trucking
- ParcelWay Independent Service Providers (ISP)
Healthcare Industry
- Community Care Facilities
- Home Health Agencies
- Hospice
- Nursing Homes

3rd drop down:
Risk Management
- Claims Management
- Compliance & Risk Management

4th drop down
Request a quote

5th drop down
About Us

6th drop down
Contact US

Target Market(s)

Potential clients

Industry/Entity Type

Business Insurance

Coding

Coded - Design and coding required

Number of Pages Required

5+ page

Colors
0054AA
0677BA
7BADD7
CADEEF
E8F1F8
00AB8E
00BBA5
67D7C9
C6EFE9
E9F9F6

Requirements
Must have
• Home Business Insurance - Commercial Auto - Employment Practice Liability Insurance - General Liability Insurance - Professional Liability Insurance - Property Insurance - Workers Compensation Insurance Industries We Serve - Construction - Janitorial - Landscapers - Manufacturing Companies - Restaurants - Towing - Trucking Healthcare Industry - Community Care Facilities - Home Health Agencies - Hospice - Nursing Homes - Risk Management - Claims Management - Compliance & Risk Management Request a Quote About Us Contact Us

```html
<!DOCTYPE html>
<html lang="en">
<head>
<meta charset="utf-8">
<title>Brookvale Insurance Services</title>
<link href="https://fonts.googleapis.com/css2?family=Poppins:wght@400;500;600&display=swap" rel="stylesheet">
<style>
:root{
  --green:#0a9a2e;
  --green-dark:#078226;
  --navy:#0b2a82;
  --navy-deep:#0a1f7a;
  --text:#3b3b3b;
  --muted:#6a6a6a;
  --soft:#f5f5f5;
  --white:#ffffff;
  --card-border:#e6e6e6;
  --star:#f2b21b;
}
*{box-sizing:border-box;margin:0;padding:0}
html,body{width:1200px;height:5000px;overflow:hidden}
body{position:relative;font-family:'Poppins',sans-serif;color:var(--text);background:var(--white)}
.abs{position:absolute}
.center{text-align:center}

/* header */
.site-header{left:0;top:0;width:1200px;height:105px;background:var(--white)}
.brand{left:95px;top:31px;width:200px;font-size:17px;line-height:21px;font-weight:600;color:var(--navy);letter-spacing:.2px}
.brand-mark{display:inline-block;width:13px;height:13px;background:var(--green);margin-right:8px;vertical-align:-1px}
.nav-link{top:44px;font-size:15px;color:#444;letter-spacing:.2px;white-space:nowrap}
.nav-link.active{color:var(--green);border-bottom:2px solid var(--green);padding-bottom:4px}
.nav-cta{left:973px;top:31px;width:142px;height:45px;background:var(--navy-deep);color:var(--white);font-size:15px;line-height:45px;text-align:center}

/* hero */
.hero{left:0;top:105px;width:1200px;height:627px;background:linear-gradient(180deg,#111 0%,#2a2a2a 45%,#6b5a4a 75%,#cfc9c3 100%)}
.hero-title{left:0;top:212px;width:1200px;font-size:49px;font-weight:500;color:var(--white);text-align:center;letter-spacing:.5px}
.hero-text{left:210px;top:298px;width:780px;font-size:15.5px;line-height:23px;color:var(--white);text-align:center}
.btn-green{background:var(--green);color:var(--white);text-align:center}
.hero-btn{left:484px;top:394px;width:231px;height:45px;line-height:45px;font-size:15px}

/* section titles */
.section-title{left:0;width:1200px;text-align:center;font-size:39px;font-weight:500;color:var(--green);letter-spacing:.5px}

/* business */
.band-soft{left:0;width:1200px;background:var(--soft)}
.service-card{width:325px;height:384px;background:var(--white);border:1px solid var(--card-border);border-radius:4px;overflow:hidden}
.service-photo{width:100%;height:210px}
.service-name{margin:22px 14px 0;font-size:17px;font-weight:500;color:var(--navy);text-align:center;line-height:22px;text-transform:uppercase}
.service-text{margin:10px 24px 0;font-size:15px;line-height:23px;color:#555;text-align:center}

/* industries */
.hub-photo{left:370px;top:1967px;width:436px;height:436px;border-radius:50%;background:radial-gradient(circle at 50% 45%,#9aa3ad,#4d5662 70%,#2f3640)}
.hub-icon{width:108px;height:108px;border-radius:50%;background:var(--green);border:3px solid var(--white);box-shadow:0 0 0 2px var(--green)}
.hub-icon svg{position:absolute;left:31px;top:31px}
.hub-label{font-size:19.5px;font-weight:600;color:var(--navy);white-space:nowrap}

/* promo banner */
.promo{left:0;top:2569px;width:1200px;height:323px;background:linear-gradient(180deg,#1d2230 0%,#2c3447 55%,#3a4a66 100%)}
.promo-title{left:0;top:2645px;width:1200px;text-align:center;font-size:40px;font-weight:500;color:var(--white)}
.promo-text{left:220px;top:2715px;width:760px;text-align:center;font-size:15.5px;line-height:23px;color:var(--white)}
.promo-btn{left:497px;top:2797px;width:204px;height:42px;border:1px solid var(--white);color:var(--white);font-size:15px;line-height:40px;text-align:center}

/* healthcare */
.care-icon{width:94px;height:94px;border-radius:50%;background:var(--green);box-shadow:0 0 0 4px var(--white),0 0 0 6px var(--green)}
.care-icon svg{position:absolute;left:27px;top:27px}
.care-name{width:260px;font-size:17px;font-weight:500;color:var(--navy);text-align:center}
.care-text{width:230px;font-size:13px;line-height:20px;color:var(--muted);text-align:center}

/* risk */
.risk-card{width:505px;height:470px;background:var(--white);box-shadow:0 2px 8px rgba(0,0,0,.08)}
.risk-photo{width:100%;height:287px}
.risk-arrow{right:36px;top:262px;width:50px;height:48px;background:var(--green)}
.risk-arrow svg{position:absolute;left:13px;top:14px}
.risk-name{left:13px;top:318px;font-size:19px;font-weight:500;color:var(--navy)}
.risk-text{left:13px;top:356px;width:480px;font-size:15px;line-height:23px;color:#444}

/* testimonials */
.review-card{width:325px;height:262px;background:var(--white);border:1px solid var(--card-border);box-shadow:0 1px 6px rgba(0,0,0,.06)}
.avatar{left:126px;top:18px;width:72px;height:72px;border-radius:50%;background:linear-gradient(135deg,#b8a089,#6b5848)}
.stars{left:0;top:96px;width:100%;text-align:center;color:var(--star);font-size:15px;letter-spacing:1px}
.reviewer{left:0;top:116px;width:100%;text-align:center;font-size:18px;color:#222}
.role{left:0;top:138px;width:100%;text-align:center;font-size:14px;font-style:italic;color:var(--green);font-weight:500}
.quote{left:14px;top:168px;width:297px;text-align:center;font-size:14px;line-height:21px;color:var(--muted)}

/* footer */
.footer{left:0;top:4496px;width:1200px;height:394px;background:var(--green)}
.foot-head{font-size:20px;font-weight:400;color:var(--white)}
.foot-rule{width:44px;height:2px;background:var(--white)}
.foot-list{list-style:none;font-size:15px;color:var(--white)}
.foot-list li{height:31px}
.foot-list li::before{content:"›";margin-right:14px;font-size:18px}
.contact-icon{width:30px;height:30px;border:1.5px solid var(--white);border-radius:4px}
.contact-icon svg{position:absolute;left:5px;top:5px}
.contact-text{font-size:15px;line-height:19px;color:var(--white)}
.bottom-bar{left:0;top:4890px;width:1200px;height:110px;background:var(--navy-deep)}
.social{top:4923px;width:40px;height:40px;border-radius:50%;border:2px solid var(--white)}
.copyright{right:91px;top:4933px;font-size:15px;color:var(--white)}
</style>
</head>
<body>

<!-- Header -->
<header class="abs site-header">
  <div class="abs brand"><span class="brand-mark"></span>Brookvale Insurance Services</div>
  <nav>
    <a class="abs nav-link active" style="left:335px">HOME</a>
    <a class="abs nav-link" style="left:413px">BUSINESS INSURANCE</a>
    <a class="abs nav-link" style="left:604px">INDUSTRIES WE SERVE</a>
    <a class="abs nav-link" style="left:800px">RISK MANAGEMENT</a>
    <a class="abs nav-cta">CONTACT US</a>
  </nav>
</header>

<!-- Hero -->
<section class="abs hero" role="img" aria-label="Business partners stacking hands over documents on a desk"></section>
<h1 class="abs hero-title">AFFORDABLE &amp; TRUSTABLE INSURANCE</h1>
<p class="abs hero-text">Lorem ipsum dolor sit amet, consectetur adipiscing elit, sed do eiusmod tempor incididunt ut labore et dolore magna aliqua. Quis ipsum suspendisse ultrices gravida. Risus commodo viverra maecenas accumsan lacus vel facilisis.</p>
<a class="abs btn-green hero-btn">REQUEST A QUOTE</a>

<!-- Business insurance -->
<section class="abs band-soft" style="top:732px;height:1070px"></section>
<h2 class="abs section-title" style="top:820px">BUSINESS INSURANCE</h2>

<article class="abs service-card" style="left:99px;top:922px">
  <div class="service-photo" role="img" aria-label="Gloved hands holding toy cars and coins" style="background:linear-gradient(135deg,#7fc3b5,#4f9e92)"></div>
  <h3 class="service-name">Commercial Auto</h3>
  <p class="service-text">Lorem ipsum dolor sit consectetur adipiscing elit, sed do accumsan lacus vel facilisis.</p>
</article>
<article class="abs service-card" style="left:443px;top:922px">
  <div class="service-photo" role="img" aria-label="Hands passing a document across a desk" style="background:linear-gradient(135deg,#8e8e8e,#dcd6cf)"></div>
  <h3 class="service-name">Employment Practice Liability Insurance</h3>
  <p class="service-text" style="margin-top:4px">Lorem ipsum dolor sit consectetur adipiscing elit, sed do accumsan lacus vel facilisis.</p>
</article>
<article class="abs service-card" style="left:785px;top:922px">
  <div class="service-photo" role="img" aria-label="Two colleagues reviewing paperwork at a table" style="background:linear-gradient(135deg,#cfcfcf,#6d6d6d)"></div>
  <h3 class="service-name">General Liability Insurance</h3>
  <p class="service-text">Lorem ipsum dolor sit consectetur adipiscing elit, sed do accumsan lacus vel facilisis.</p>
</article>
<article class="abs service-card" style="left:99px;top:1326px">
  <div class="service-photo" role="img" aria-label="Agent meeting a couple in a home" style="background:linear-gradient(135deg,#d9d2c8,#8a7a6a)"></div>
  <h3 class="service-name">Professional Liability Insurance</h3>
  <p class="service-text" style="margin-top:4px">Lorem ipsum dolor sit consectetur adipiscing elit, sed do accumsan lacus vel facilisis.</p>
</article>
<article class="abs service-card" style="left:443px;top:1326px">
  <div class="service-photo" role="img" aria-label="Hand resting on a property insurance form" style="background:linear-gradient(135deg,#9a9a9a,#e6e6e6)"></div>
  <h3 class="service-name">Property Insurance</h3>
  <p class="service-text">Lorem ipsum dolor sit consectetur adipiscing elit, sed do accumsan lacus vel facilisis.</p>
</article>
<article class="abs service-card" style="left:785px;top:1326px">
  <div class="service-photo" role="img" aria-label="Silver car parked outdoors" style="background:linear-gradient(135deg,#5d6a55,#2f3a42)"></div>
  <h3 class="service-name">Workers Compensation Insurance</h3>
  <p class="service-text" style="margin-top:4px">Lorem ipsum dolor sit consectetur adipiscing elit, sed do accumsan lacus vel facilisis.</p>
</article>

<!-- Industries -->
<h2 class="abs section-title" style="top:1860px">INDUSTRIES WE SERVE</h2>
<div class="abs hub-photo" role="img" aria-label="Business team working together at a desk"></div>

<div class="abs hub-icon" style="left:408px;top:1944px"><svg width="40" height="40" viewBox="0 0 40 40" fill="none" stroke="#fff" stroke-width="2.5"><circle cx="20" cy="12" r="6"/><path d="M8 36c0-8 5-13 12-13s12 5 12 13z"/></svg></div>
<div class="abs hub-icon" style="left:661px;top:1944px"><svg width="40" height="40" viewBox="0 0 40 40" fill="none" stroke="#fff" stroke-width="2.5"><path d="M10 16a10 10 0 0 1 20 0z"/><circle cx="20" cy="22" r="5"/><path d="M8 38c0-7 5-11 12-11s12 4 12 11"/></svg></div>
<div class="abs hub-icon" style="left:323px;top:2106px"><svg width="40" height="40" viewBox="0 0 40 40" fill="none" stroke="#fff" stroke-width="2.5"><circle cx="13" cy="16" r="5"/><circle cx="27" cy="16" r="5"/><path d="M4 32c0-5 4-8 9-8s9 3 9 8M18 32c0-5 4-8 9-8s9 3 9 8"/></svg></div>
<div class="abs hub-icon" style="left:746px;top:2106px"><svg width="40" height="40" viewBox="0 0 40 40" fill="none" stroke="#fff" stroke-width="2.5"><rect x="6" y="14" width="20" height="20"/><path d="M26 22h8v12h-8M12 14V6h8v8"/></svg></div>
<div class="abs hub-icon" style="left:367px;top:2261px"><svg width="40" height="40" viewBox="0 0 40 40" fill="none" stroke="#fff" stroke-width="2.5"><circle cx="12" cy="12" r="5"/><path d="M4 34c0-7 4-11 9-11"/><rect x="18" y="18" width="18" height="14"/></svg></div>
<div class="abs hub-icon" style="left:701px;top:2261px"><svg width="40" height="40" viewBox="0 0 40 40" fill="none" stroke="#fff" stroke-width="2.5"><rect x="4" y="14" width="20" height="14"/><path d="M24 18h7l5 6v4H24z"/><circle cx="11" cy="31" r="3"/><circle cx="30" cy="31" r="3"/></svg></div>
<div class="abs hub-icon" style="left:534px;top:2350px"><svg width="40" height="40" viewBox="0 0 40 40" fill="none" stroke="#fff" stroke-width="2.5"><rect x="6" y="10" width="12" height="26"/><rect x="18" y="4" width="16" height="32"/><path d="M22 10h8M22 16h8M22 22h8M10 16h4M10 22h4"/></svg></div>

<span class="abs hub-label" style="right:806px;top:1985px">LANDSCAPERS</span>
<span class="abs hub-label" style="left:786px;top:1985px">CONSTRUCTION</span>
<span class="abs hub-label" style="right:891px;top:2147px">RESTAURANTS</span>
<span class="abs hub-label" style="left:870px;top:2147px">JANITORIAL</span>
<span class="abs hub-label" style="right:854px;top:2302px">TOWING</span>
<span class="abs hub-label" style="left:829px;top:2302px">TRUCKING</span>
<span class="abs hub-label center" style="left:388px;top:2468px;width:400px">MANUFACTURING COMPANIES</span>

<!-- Promo banner -->
<section class="abs promo" role="img" aria-label="Modern house exterior at dusk"></section>
<h2 class="abs promo-title">POPULAR INSURANCE AGENCY SERVICES</h2>
<p class="abs promo-text">Our best-selling AquaStride swim spas redefine the traditional swimming pool experience with powerful exercise and therapy features.</p>
<a class="abs promo-btn">Request A Quote</a>

<!-- Healthcare -->
<section class="abs band-soft" style="top:2892px;height:444px"></section>
<h2 class="abs section-title" style="top:2957px">HEALTHCARE INDUSTRY</h2>

<div class="abs care-icon" style="left:167px;top:3041px"><svg width="40" height="40" viewBox="0 0 40 40" fill="none" stroke="#fff" stroke-width="2.5"><path d="M20 4l14 5v10c0 9-6 15-14 18C12 34 6 28 6 19V9z"/><path d="M20 13l2.5 5 5.5.5-4 3.8 1 5.5-5-2.7-5 2.7 1-5.5-4-3.8 5.5-.5z"/></svg></div>
<div class="abs care-icon" style="left:419px;top:3041px"><svg width="40" height="40" viewBox="0 0 40 40" fill="none" stroke="#fff" stroke-width="2.5"><circle cx="16" cy="22" r="6"/><circle cx="16" cy="22" r="11" stroke-dasharray="4 3"/><circle cx="30" cy="10" r="4"/></svg></div>
<div class="abs care-icon" style="left:664px;top:3041px"><svg width="40" height="40" viewBox="0 0 40 40" fill="none" stroke="#fff" stroke-width="2.2"><circle cx="20" cy="20" r="3"/><ellipse cx="20" cy="20" rx="16" ry="6"/><ellipse cx="20" cy="20" rx="16" ry="6" transform="rotate(60 20 20)"/><ellipse cx="20" cy="20" rx="16" ry="6" transform="rotate(120 20 20)"/></svg></div>
<div class="abs care-icon" style="left:941px;top:3041px"><svg width="40" height="40" viewBox="0 0 40 40" fill="none" stroke="#fff" stroke-width="2.5"><circle cx="16" cy="22" r="6"/><circle cx="16" cy="22" r="11" stroke-dasharray="4 3"/><circle cx="30" cy="10" r="4"/></svg></div>

<h3 class="abs care-name" style="left:84px;top:3165px">COMMUNITY CARE FACILITIES</h3>
<h3 class="abs care-name" style="left:336px;top:3165px">NURSING HOMES</h3>
<h3 class="abs care-name" style="left:581px;top:3165px">HOSPICE</h3>
<h3 class="abs care-name" style="left:858px;top:3165px">HOME HEALTH AGENCIES</h3>
<p class="abs care-text" style="left:99px;top:3203px">We know the area and the market and we're part of your community, not a bot on the net .</p>
<p class="abs care-text" style="left:351px;top:3203px">We work to close your loan as quickly as possible. We can even hit curveballs!</p>
<p class="abs care-text" style="left:596px;top:3203px">We offer a hybrid approach of new technology to speed closing and old communication.</p>
<p class="abs care-text" style="left:873px;top:3203px">We have the latest online tech like secure mobile uploading and we're old-fashioned way too!</p>

<!-- Risk management -->
<h2 class="abs section-title" style="top:3378px;left:-14px">RISK MANAGEMENT</h2>
<article class="abs risk-card" style="left:89px;top:3461px">
  <div class="risk-photo" role="img" aria-label="Couple relaxing on a sofa with a laptop among moving boxes" style="background:linear-gradient(135deg,#d8cfc2,#8aa0b3)"></div>
  <div class="abs risk-arrow"><svg width="24" height="20" viewBox="0 0 24 20" fill="none" stroke="#fff" stroke-width="2.5"><path d="M2 10h19M14 3l7 7-7 7"/></svg></div>
  <h3 class="abs risk-name">CLAIMS MANAGEMENT</h3>
  <p class="abs risk-text">Today's market is fluid. We have resources to shop many find the right loan to fit your needs.</p>
</article>
<article class="abs risk-card" style="left:604px;top:3461px">
  <div class="risk-photo" role="img" aria-label="Couple meeting an advisor at a table" style="background:linear-gradient(135deg,#cfd4c8,#6f7a70)"></div>
  <div class="abs risk-arrow"><svg width="24" height="20" viewBox="0 0 24 20" fill="none" stroke="#fff" stroke-width="2.5"><path d="M2 10h19M14 3l7 7-7 7"/></svg></div>
  <h3 class="abs risk-name">COMPLIANCE &amp; RISK MANAGEMENT</h3>
  <p class="abs risk-text">Our goal is to close your loan in 14 days or less! With our digital also helps avoid unnecessary delays.</p>
</article>

<!-- Testimonials -->
<h2 class="abs section-title" style="top:4070px;left:0">WHAT OUR CLIENTS SAYS</h2>
<article class="abs review-card" style="left:103px;top:4160px">
  <div class="abs avatar" role="img" aria-label="Client portrait"></div>
  <div class="abs stars">★★★★★</div>
  <div class="abs reviewer">Dana Whitfield</div>
  <div class="abs role">Organiser</div>
  <p class="abs quote">We don't place you into a loan profile each customer as an formula created by the banking industry.</p>
</article>
<article class="abs review-card" style="left:445px;top:4160px">
  <div class="abs avatar" role="img" aria-label="Client portrait" style="background:linear-gradient(135deg,#e0b540,#4a4a4a)"></div>
  <div class="abs stars">★★★★★</div>
  <div class="abs reviewer">Dana Whitfield</div>
  <div class="abs role">Organiser</div>
  <p class="abs quote">We don't place you into a loan profile each customer as an formula created by the banking industry.</p>
</article>
<article class="abs review-card" style="left:787px;top:4160px">
  <div class="abs avatar" role="img" aria-label="Client portrait" style="background:linear-gradient(135deg,#d9d0c8,#5a4538)"></div>
  <div class="abs stars">★★★★★</div>
  <div class="abs reviewer">Dana Whitfield</div>
  <div class="abs role">Organiser</div>
  <p class="abs quote">We don't place you into a loan profile each customer as an formula created by the banking industry.</p>
</article>

<!-- Footer -->
<footer class="abs footer">
  <h4 class="abs foot-head" style="left:214px;top:85px">Quick Links</h4>
  <div class="abs foot-rule" style="left:214px;top:129px"></div>
  <ul class="abs foot-list" style="left:220px;top:170px">
    <li>Home</li><li>About Us</li><li>Our Services</li><li>Our Blogs</li><li>Testimonials</li>
  </ul>

  <h4 class="abs foot-head" style="left:454px;top:85px">Services</h4>
  <div class="abs foot-rule" style="left:454px;top:129px"></div>
  <ul class="abs foot-list" style="left:460px;top:170px">
    <li>Construction</li><li>Janitorial</li><li>Landscapers</li><li>Manufacturing Companies</li><li>Restaurants</li>
  </ul>

  <h4 class="abs foot-head" style="left:765px;top:83px">Contact Us</h4>
  <div class="abs contact-icon" style="left:770px;top:175px"><svg width="18" height="18" viewBox="0 0 18 18" fill="none" stroke="#fff" stroke-width="1.6"><path d="M4 2l3 3-2 2c1 2 3 4 5 5l2-2 3 3-2 2C8 15 3 10 2 4z"/></svg></div>
  <p class="abs contact-text" style="left:820px;top:173px">CALL US<br>(818) 555-0193</p>
  <div class="abs contact-icon" style="left:770px;top:231px"><svg width="18" height="18" viewBox="0 0 18 18" fill="none" stroke="#fff" stroke-width="1.6"><rect x="2" y="4" width="14" height="10"/><path d="M2 4l7 6 7-6"/></svg></div>
  <p class="abs contact-text" style="left:820px;top:229px">EMAIL US<br>info@brookvaleinsure.com</p>
  <div class="abs contact-icon" style="left:770px;top:287px"><svg width="18" height="18" viewBox="0 0 18 18" fill="none" stroke="#fff" stroke-width="1.6"><path d="M9 16s5-5 5-9a5 5 0 0 0-10 0c0 4 5 9 5 9z"/><circle cx="9" cy="7" r="1.8"/></svg></div>
  <p class="abs contact-text" style="left:820px;top:285px">7316 Marlowe Ave Unit D, Studio City<br>Ca 91607</p>
</footer>

<div class="abs bottom-bar"></div>
<span class="abs social" style="left:87px" aria-label="Social link"></span>
<span class="abs social" style="left:139px" aria-label="Social link"></span>
<span class="abs social" style="left:192px" aria-label="Social link"></span>
<span class="abs social" style="left:244px" aria-label="Social link"></span>
<p class="abs copyright">All rightsreserved. Copyrights @ 20224</p>

</body>
</html>
```